Geschäftspapiere für Unternehmen aus Not- und Sicherheitsbeleuchtungsbranche
Zielgruppe
Wir sind ein Unternehmen der Not- und Sicherheitsbeleuchtungsbranche und arbeiten vornehmlich mit dem deutschen Elektrogroßhandel zusammen.
Aufgabenstellung
WIr möchten nicht nur Schreibblöcke drucken, wir benötigen die Vorlage auch als Word-Datei für Geschäftsbriefe.
Orientierung und Farbwahl gemäß unserer Website. Im Anhang finden Sie bereits das aktuelle Briefdesign. Dieses verbraucht jedoch zu viel Platz und liegt uns nicht als Word vor. Die Daten können übernommen werden, ergänzt muss noch die UST-ID werden: DE718206359

```html
<!DOCTYPE html>
<html lang="de">
<head>
<meta charset="utf-8">
<title>Lumora Systems – Briefbogen</title>
<link rel="stylesheet" href="https://fonts.googleapis.com/css2?family=Montserrat:wght@400;500;700&display=swap">
<style>
  :root {
    --bg: #e3e8ea;
    --paper: #ffffff;
    --magenta: #b0046c;
    --slate: #5f6670;
    --ink: #2a2d31;
    --muted: #4a4f56;
    --ghost: #ececee;
  }
  * { margin: 0; padding: 0; box-sizing: border-box; }
  html, body { width: 1200px; height: 949px; overflow: hidden; background: var(--bg); }
  body { font-family: "Montserrat", sans-serif; color: var(--ink); }

  .letterhead {
    position: absolute; left: 289px; top: 34px;
    width: 622px; height: 880px;
    background: var(--paper);
    box-shadow: 0 6px 18px rgba(0,0,0,.12);
    overflow: hidden;
  }

  .sender-line {
    position: absolute; left: 58px; top: 128px;
    font-size: 6.5px; padding-bottom: 2px;
    border-bottom: 1.5px solid var(--magenta);
    white-space: nowrap;
  }

  .brand {
    position: absolute; right: 40px; top: 58px;
    display: flex; align-items: center; gap: 8px;
    font-size: 20px; font-weight: 500; letter-spacing: 3px; color: var(--slate);
  }
  .brand-square { width: 22px; height: 22px; border: 3px solid var(--slate); }

  .contact-card {
    position: absolute; right: 40px; top: 104px; width: 130px;
    padding-left: 10px; border-left: 1.5px solid var(--slate);
    font-size: 8px; line-height: 1.45; font-style: normal;
  }
  .contact-card .company { color: var(--magenta); font-weight: 700; }
  .icon-row { display: flex; align-items: center; gap: 4px; white-space: nowrap; }
  .icon-row svg { width: 7px; height: 7px; flex: none; }

  .watermark {
    position: absolute; left: 90px; top: 360px;
    display: flex; align-items: center; gap: 24px;
    font-size: 62px; font-weight: 400; letter-spacing: 10px; color: var(--ghost);
  }
  .watermark-square { width: 110px; height: 110px; border: 14px solid var(--ghost); }

  .footer-text {
    position: absolute; font-size: 6.5px; line-height: 1.45;
    color: var(--muted); white-space: nowrap; font-style: normal;
  }
  .footer-text strong { color: var(--ink); font-weight: 700; }
  .footer-text .accent { color: var(--magenta); font-weight: 700; }
  .f-company  { left: 58px;  top: 768px; }
  .f-director { left: 158px; top: 776px; }
  .f-contact  { left: 242px; top: 782px; }
  .f-register { left: 348px; top: 788px; }
  .f-bank     { left: 438px; top: 794px; }

  .footer-bands { position: absolute; left: 0; bottom: 0; width: 622px; height: 62px; }
</style>
</head>
<body>
  <main class="letterhead">
    <p class="sender-line">Lumora Systems GmbH • Lindenweg 7 • D-83417 Seebruck</p>

    <div class="brand"><span class="brand-square"></span>LUMORA</div>

    <address class="contact-card">
      <div class="company">Lumora Systems GmbH</div>
      <div>Lindenweg 7</div>
      <div>D-83417 Seebruck</div>
      <div class="icon-row">
        <svg viewBox="0 0 10 10"><path d="M2 1h2l1 2.5-1.3 1a6 6 0 0 0 2.8 2.8l1-1.3L10 7v2a1 1 0 0 1-1 1A9 9 0 0 1 1 2a1 1 0 0 1 1-1z" fill="#b0046c"/></svg>08667 31862 40</div>
      <div class="icon-row">
        <svg viewBox="0 0 10 10"><rect x="0" y="2" width="10" height="6" fill="#b0046c"/><path d="M0 2l5 3.5L10 2" stroke="#fff" fill="none"/></svg>info@lumora-systems.de</div>
      <div class="icon-row">
        <svg viewBox="0 0 10 10"><circle cx="5" cy="5" r="4.5" fill="#b0046c"/><path d="M0.5 5h9M5 .5c-2 2.5-2 6.5 0 9M5 .5c2 2.5 2 6.5 0 9" stroke="#fff" stroke-width=".7" fill="none"/></svg>www.lumora-systems.de</div>
    </address>

    <div class="watermark" aria-hidden="true"><span class="watermark-square"></span>LUMORA</div>

    <address class="footer-text f-company"><strong>Lumora Systems GmbH</strong><br>Lindenweg 7<br>D-83417 Seebruck</address>
    <div class="footer-text f-director"><span class="accent">Geschäftsführer</span><br>Moritz Kelbing<br>Managing Director</div>
    <div class="footer-text f-contact">
      <div class="icon-row"><svg viewBox="0 0 10 10"><path d="M2 1h2l1 2.5-1.3 1a6 6 0 0 0 2.8 2.8l1-1.3L10 7v2a1 1 0 0 1-1 1A9 9 0 0 1 1 2a1 1 0 0 1 1-1z" fill="#b0046c"/></svg>08667 31862 40</div>
      <div class="icon-row"><svg viewBox="0 0 10 10"><rect x="0" y="2" width="10" height="6" fill="#b0046c"/></svg>info@lumora-systems.de</div>
      <div class="icon-row"><svg viewBox="0 0 10 10"><circle cx="5" cy="5" r="4.5" fill="#b0046c"/></svg>www.lumora-systems.de</div>
    </div>
    <div class="footer-text f-register">Amtsgericht Rosenheim<br>HRB 40527<br>USt-ID DE718206359</div>
    <div class="footer-text f-bank">Bankverbindung Seenland Bank eG<br>BLZ 700 123 45<br>IBAN: DE42 7001 2345 0061 3379 05<br>BIC: SEENDEM1XXX</div>

    <svg class="footer-bands" viewBox="0 0 622 62" preserveAspectRatio="none" aria-hidden="true">
      <polygon points="0,6 262,6 254,18 0,18" fill="var(--magenta)"/>
      <polygon points="268,24 622,24 622,62 248,62 262,40" fill="var(--slate)"/>
    </svg>
  </main>
</body>
</html>
```